Company Values - print for wall

We ned a print of our values on one of the walls in our office. Create a couple of suggestions that we can print on our walls.

Summary:
- See power point with values
- make two suggestion: one with only titles + one with titles and bulletpoints / use the "We" version)
- make a suggestion in a moon raiders theme
- see brand book for inspiration
- see images of office for inspiration
Updates

The company's values that we want to highlight are: 1. Exceed expectations 2. Execute with passion 3. Empower each other Exceed expectations:​ • We establish a good understanding of current expectations.​ • We provide helpful, honest, and timely feedback.​ • We deliver impressive quality.​ Execute with passion:​ • We embrace change.​ • We seek innovative solutions.​ • We inspire others with your actions and attitudes. ​ • We care about success. ​ • We are confident and humble. Empower each other:​ • We are available to help colleagues.​ • We are open-minded.​ • We seek and share information proactively.​ • We respect others’ time.​ This is in line with achieving the company vision: « Our vision is to make a difference for our customers through our highly customizable solutions for planning, execution, and analysis. It’s less about the software itself and more about customer success. Make better decisions faster with Clearmont. »​ Eirik Tove Malmberg, CEO Clearmont Company slogan: Better Decisions Faster​ It's a lot of text above, but what we what to emphasize most are the following text above and here again: exceed expectations, execute with passion, empower each other We can do something fun and cool with the Moon Raiders theme as this is internal - that's the visual that would work with the company culture.

Font styles to use
Sans Serif

Requirements
Nice to have
• - one suggestion with Montserrat font
- one suggestion in moon raiders font

```html
<!DOCTYPE html>
<html lang="en">
<head>
<meta charset="utf-8">
<title>Clearmont – Company Values Wall Print Options</title>
<link href="https://fonts.googleapis.com/css2?family=Bebas+Neue&family=Montserrat:wght@500;600;800&family=Arimo:wght@400;700&family=PT+Sans:wght@700&display=swap" rel="stylesheet">
<style>
  :root {
    --board-top: #4a4e4e;
    --board-bottom: #2b2d2e;
    --paper: #ffffff;
    --navy: #1d3c7c;
    --navy-deep: #0c2670;
    --band-start: #0b2567;
    --band-end: #1f4ea2;
    --orange: #f99a45;
    --coral: #ec5a55;
    --teal: #00b8c2;
    --label: #f2f2f2;
    --body: #ffffff;
  }
  * { margin: 0; padding: 0; box-sizing: border-box; }
  html, body { width: 1200px; height: 877px; overflow: hidden; }
  body {
    background: linear-gradient(180deg, var(--board-top), var(--board-bottom));
    position: relative;
    font-family: "Montserrat", sans-serif;
  }
  .option-label {
    position: absolute;
    top: 44px;
    width: 535px;
    text-align: center;
    font-family: "PT Sans", sans-serif;
    font-weight: 700;
    font-size: 20px;
    color: var(--label);
  }
  .poster {
    position: absolute;
    top: 85px;
    width: 535px;
    height: 756px;
    background: var(--paper);
    box-shadow: 0 6px 18px rgba(0,0,0,.55);
    overflow: hidden;
  }
  .option-one { left: 58px; }
  .option-two { left: 613px; }

  .brand-name {
    position: absolute;
    top: 28px;
    left: 0;
    width: 100%;
    text-align: center;
    font-family: "Montserrat", sans-serif;
    font-weight: 800;
    font-size: 44px;
    letter-spacing: -1px;
    color: var(--navy);
    line-height: 1;
  }
  .headline {
    position: absolute;
    top: 96px;
    left: 0;
    width: 535px;
    height: 80px;
  }
  .artwork {
    position: absolute;
    left: 0;
    top: 0;
    width: 535px;
    height: 571px;
  }

  .value-list {
    position: absolute;
    left: 328px;
    width: 200px;
    color: var(--navy);
  }
  .value-title {
    font-weight: 800;
    font-size: 12.6px;
    letter-spacing: .2px;
    line-height: 14px;
  }
  .value-points { list-style: none; }
  .value-points li {
    font-weight: 500;
    font-size: 9.7px;
    line-height: 11.9px;
    padding-left: 8px;
    text-indent: -6px;
  }
  .value-points li::before { content: "• "; font-size: 7px; }

  .vision-band {
    position: absolute;
    left: 0;
    top: 571px;
    width: 535px;
    height: 185px;
    background: linear-gradient(160deg, var(--band-start), var(--band-end));
  }
  .vision-copy {
    position: absolute;
    left: 40px;
    width: 457px;
    font-family: "Arimo", sans-serif;
    font-size: 10.6px;
    line-height: 12.8px;
    color: var(--body);
    text-align: justify;
  }
  .vision-copy strong {
    font-family: "Montserrat", sans-serif;
    font-weight: 800;
  }
  .vision-statement { top: 20px; }
  .slogan-statement { top: 85px; }
  .web-tab {
    position: absolute;
    left: 165px;
    bottom: 0;
    width: 207px;
    height: 28px;
    background: var(--coral);
    clip-path: polygon(4% 0, 96% 0, 100% 100%, 0 100%);
    border-radius: 6px 6px 0 0;
    color: #fff;
    font-family: "Arimo", sans-serif;
    font-size: 13px;
    line-height: 28px;
    text-align: center;
  }
</style>
</head>
<body>

<div class="option-label" style="left:54px">Option one</div>
<div class="option-label" style="left:609px">Option Two</div>

<!-- Option one: numeral layout with bullet points -->
<section class="poster option-one">
  <div class="brand-name">clearmont</div>

  <svg class="headline" viewBox="0 0 535 80" aria-label="Company Values">
    <defs>
      <linearGradient id="titleFillA" x1="0" x2="1" y1="0" y2="0">
        <stop offset="0" stop-color="#f59a4a"/>
        <stop offset="1" stop-color="#ec5657"/>
      </linearGradient>
    </defs>
    <text x="46" y="73" textLength="446" lengthAdjust="spacingAndGlyphs" font-family="Bebas Neue, sans-serif" font-size="92" fill="#d9d9d9">COMPANY VALUES</text>
    <text x="43" y="71" textLength="446" lengthAdjust="spacingAndGlyphs" font-family="Bebas Neue, sans-serif" font-size="92" fill="url(#titleFillA)">COMPANY VALUES</text>
  </svg>

  <svg class="artwork" viewBox="0 0 535 571">
    <defs>
      <linearGradient id="pinOrange" x1="0" y1="0" x2="1" y2="1">
        <stop offset="0" stop-color="#f7a44a"/><stop offset="1" stop-color="#ec5a55"/>
      </linearGradient>
      <linearGradient id="pinTeal" x1="0" y1="0" x2="1" y2="1">
        <stop offset="0" stop-color="#1a8fd6"/><stop offset="1" stop-color="#00bcc4"/>
      </linearGradient>
      <linearGradient id="pinNavy" x1="0" y1="0" x2="1" y2="1">
        <stop offset="0" stop-color="#0f2f82"/><stop offset="1" stop-color="#19bcc7"/>
      </linearGradient>
    </defs>

    <g class="numeral-three" aria-label="3">
      <path fill="var(--orange)" d="M46,306 L46,272 C46,222 85,193 133,193 C184,193 221,222 221,272 L221,306 L161,306 L161,276 C161,263 150,255 131,255 C112,255 101,263 101,276 L101,306 Z"/>
      <path fill="var(--teal)" d="M161,309 L221,309 C221,333 205,356 181,373 C205,391 221,420 221,446 L101,446 L101,350 L161,350 Z"/>
      <path fill="var(--navy-deep)" d="M46,449 L101,449 L101,505 C101,518 112,525 131,525 C150,525 161,518 161,505 L161,449 L221,449 L221,520 C221,565 185,590 133,590 C80,590 46,565 46,520 Z"/>
    </g>

    <g class="value-pin">
      <line x1="221" y1="261" x2="236" y2="261" stroke="#f59a4a" stroke-width="1.5"/>
      <path d="M231,261 L258,236 A33 33 0 1 1 258,286 Z" fill="url(#pinOrange)"/>
      <circle cx="278" cy="261" r="26" fill="#fff"/>
      <circle cx="278" cy="261" r="17" fill="#fbe1d6" role="img" aria-label="Icon of a person climbing steps toward rising arrows and a coin"/>
    </g>
    <g class="value-pin">
      <line x1="181" y1="373" x2="236" y2="373" stroke="#16a9cf" stroke-width="1.5"/>
      <path d="M231,373 L258,348 A33 33 0 1 1 258,398 Z" fill="url(#pinTeal)"/>
      <circle cx="278" cy="373" r="26" fill="#fff"/>
      <circle cx="278" cy="373" r="17" fill="#d5eef5" role="img" aria-label="Icon of three people above a raised fist"/>
    </g>
    <g class="value-pin">
      <line x1="221" y1="486" x2="236" y2="486" stroke="#123a8a" stroke-width="1.5"/>
      <path d="M231,486 L258,461 A33 33 0 1 1 258,511 Z" fill="url(#pinNavy)"/>
      <circle cx="278" cy="486" r="26" fill="#fff"/>
      <circle cx="278" cy="486" r="17" fill="#d8deee" role="img" aria-label="Icon of two hands sheltering a heart"/>
    </g>
  </svg>

  <div class="value-list" style="top:224px">
    <h2 class="value-title">EXCEED EXPECTATIONS</h2>
    <ul class="value-points">
      <li>We establish a good understand ing of current expectations.</li>
      <li>We provide helpful, honest, and timely feedback.</li>
      <li>We deliver impressive quality.</li>
    </ul>
  </div>
  <div class="value-list" style="top:335px; width:205px">
    <h2 class="value-title">EMPOWER EACH OTHER</h2>
    <ul class="value-points">
      <li>We are available to help coleagues.</li>
      <li>We are open-minded.</li>
      <li>We seek and share information proactively.</li>
      <li>We respect others’ time.</li>
    </ul>
  </div>
  <div class="value-list" style="top:443px">
    <h2 class="value-title">EXECUTE WITH PASSION</h2>
    <ul class="value-points">
      <li>We embrace change.</li>
      <li>We seek innovative solutions.</li>
      <li>We inspire others with your actions and attitudes.</li>
      <li>We care about success.</li>
      <li>We are confident and humble.</li>
    </ul>
  </div>

  <div class="vision-band">
    <p class="vision-copy vision-statement"><strong>COMPANY VISION:</strong> « Our vision is to make a difference for our customers through our highly customizable solutions for planning, execution, and analysis. It’s less about the software itself and more about customer success. Make better decisions faster with Clearmont. » Eirik Tove Malmberg, CEO</p>
    <p class="vision-copy slogan-statement"><strong>CLEARMONT COMPANY SLOGAN:</strong> Better Decisions Faster It's a lot of text above, but what we what to emphasize most are the following text above and here again: exceed expectations, execute with passion, empower each other We can do something fun and cool with the Moon Raiders theme as this is internal - that's the visual that would work with the company culture.</p>
    <div class="web-tab">www.clearmont.com</div>
  </div>
</section>

<!-- Option two: circular values diagram -->
<section class="poster option-two">
  <div class="brand-name">clearmont</div>

  <svg class="headline" viewBox="0 0 535 80" aria-label="Company Values">
    <defs>
      <linearGradient id="titleFillB" x1="0" x2="1" y1="0" y2="0">
        <stop offset="0" stop-color="#f59a4a"/>
        <stop offset="1" stop-color="#ec5657"/>
      </linearGradient>
    </defs>
    <text x="46" y="73" textLength="446" lengthAdjust="spacingAndGlyphs" font-family="Bebas Neue, sans-serif" font-size="92" fill="#d9d9d9">COMPANY VALUES</text>
    <text x="43" y="71" textLength="446" lengthAdjust="spacingAndGlyphs" font-family="Bebas Neue, sans-serif" font-size="92" fill="url(#titleFillB)">COMPANY VALUES</text>
  </svg>

  <svg class="artwork" viewBox="0 0 535 571">
    <defs>
      <linearGradient id="ringOrange" gradientUnits="userSpaceOnUse" x1="150" y1="440" x2="270" y2="240">
        <stop offset="0" stop-color="#ec5a55"/><stop offset="1" stop-color="#f7a04a"/>
      </linearGradient>
      <linearGradient id="ringBlue" gradientUnits="userSpaceOnUse" x1="270" y1="240" x2="390" y2="430">
        <stop offset="0" stop-color="#2f8ccf"/><stop offset="1" stop-color="#27bcc6"/>
      </linearGradient>
      <linearGradient id="ringShadow" x1="0" y1="0" x2="1" y2="1">
        <stop offset="0" stop-color="#000" stop-opacity=".12"/><stop offset="1" stop-color="#000" stop-opacity="0"/>
      </linearGradient>
      <path id="arcExceed" d="M161.2,430.8 A126 126 0 0 1 263.6,238.1"/>
      <path id="arcEmpower" d="M272.4,238.1 A126 126 0 0 1 379.3,423.1"/>
      <path id="arcExecute" d="M374.8,430.8 A126 126 0 0 1 166.1,438.1"/>
    </defs>

    <path d="M360,275 L535,450 L535,571 L330,420 Z" fill="url(#ringShadow)"/>

    <path d="M161.2,430.8 A126 126 0 0 1 263.6,238.1" fill="none" stroke="url(#ringOrange)" stroke-width="93"/>
    <path d="M272.4,238.1 A126 126 0 0 1 379.3,423.1" fill="none" stroke="url(#ringBlue)" stroke-width="93"/>
    <path d="M374.8,430.8 A126 126 0 0 1 166.1,438.1" fill="none" stroke="var(--navy-deep)" stroke-width="98"/>

    <g font-family="Montserrat, sans-serif" font-weight="800" font-size="12.5" fill="#fff" letter-spacing=".5">
      <text dominant-baseline="middle"><textPath href="#arcExceed" startOffset="50%" text-anchor="middle">EXCEED EXPECTATIONS</textPath></text>
      <text dominant-baseline="middle"><textPath href="#arcEmpower" startOffset="50%" text-anchor="middle">EMPOWER EACH OTHER</textPath></text>
      <text dominant-baseline="middle"><textPath href="#arcExecute" startOffset="50%" text-anchor="middle">EXECUTE WITH PASSION</textPath></text>
    </g>

    <circle cx="268" cy="364" r="66" fill="#e4e4e6"/>
    <circle cx="268" cy="364" r="53" fill="#fff"/>
    <circle cx="268" cy="364" r="34" fill="#fde3d6" role="img" aria-label="Icon of two open hands lifting a person"/>

    <circle cx="268" cy="242" r="33" fill="#f7994a"/>
    <circle cx="268" cy="242" r="27" fill="#fff"/>
    <circle cx="268" cy="242" r="17" fill="#fbe1d6" role="img" aria-label="Icon of a person climbing steps toward rising arrows and a coin"/>

    <circle cx="375" cy="420" r="36" fill="var(--teal)"/>
    <circle cx="375" cy="420" r="28" fill="#fff"/>
    <circle cx="375" cy="420" r="17" fill="#d5eef5" role="img" aria-label="Icon of three people above a raised fist"/>

    <circle cx="161" cy="424" r="38" fill="var(--navy-deep)"/>
    <circle cx="161" cy="424" r="29" fill="#fff"/>
    <circle cx="161" cy="424" r="17" fill="#d8deee" role="img" aria-label="Icon of two hands sheltering a heart"/>
  </svg>

  <div class="vision-band">
    <p class="vision-copy vision-statement"><strong>COMPANY VISION:</strong> « Our vision is to make a difference for our customers through our highly customizable solutions for planning, execution, and analysis. It’s less about the software itself and more about customer success. Make better decisions faster with Clearmont. » Eirik Tove Malmberg, CEO</p>
    <p class="vision-copy slogan-statement"><strong>CLEARMONT COMPANY SLOGAN:</strong> Better Decisions Faster It's a lot of text above, but what we what to emphasize most are the following text above and here again: exceed expectations, execute with passion, empower each other We can do something fun and cool with the Moon Raiders theme as this is internal - that's the visual that would work with the company culture.</p>
    <div class="web-tab">www.clearmont.com</div>
  </div>
</section>

</body>
</html>
```